Comets Business Card Design Project

Create a standard format for letterhead and business cards. I know I can just get the layout with an example name on it, then add the names, titles and address that we want to it and give that to a printer so that the graphics are much better. Organization Mission Statement: Providing a professionally organized, structured, and supportive environment with quality development and professional coaching to inspire our student athletes, and assist them in fulfilling their dreams of achievement in academic excellence, high level competition and playing collegiate softball. Girl's Elite Fastpitch Softball

Check web site: www.brookvalediamondcomets.org
Updates

Sorry I didn't get the URL and files out when I started the project. Logo examples, mission, vision, etc. are posted now. And the URL to the web site is www.brookvalediamondcomets.org.

I'm very interested in an original creative design that is professional yet relevant to a sports team and for coaches.

Target Market(s)

college recuriters, industry product suppliers, parents, coaches, tournament directors

Industry/Entity Type

Environment

Requirements
Must have
• Use one of two logos; include the web site URL and a general mailbox for inquires. Includes Name, title, email and phone number
Nice to have
• Some color variations or background. Maybe a mission statement on the back. Maybe a QR code to the web site.

```html
<!DOCTYPE html>
<html lang="en">
<head>
<meta charset="utf-8">
<title>Brookvale Comets Business Cards</title>
<link href="https://fonts.googleapis.com/css2?family=Open+Sans:wght@400;600;700;800&display=swap" rel="stylesheet">
<style>
  :root {
    --bg: #d9d9d9;
    --card-black: #0b0b0b;
    --card-black-soft: #1c1c1c;
    --red: #c4161c;
    --red-dark: #6e0a0d;
    --white: #f2f2f2;
    --grey: #bdbdbd;
  }
  * { margin: 0; padding: 0; box-sizing: border-box; }
  html, body { width: 1200px; height: 1028px; overflow: hidden; }
  body {
    background: var(--bg);
    font-family: "Open Sans", Arial, sans-serif;
    position: relative;
  }
  .card {
    position: absolute;
    background: radial-gradient(ellipse at 35% 30%, var(--card-black-soft), var(--card-black) 70%);
    box-shadow: 0 14px 30px rgba(0,0,0,.35);
    overflow: hidden;
  }
  .card svg.swoosh { position: absolute; inset: 0; width: 100%; height: 100%; }

  /* Front card */
  .card-front { left: 50px; top: 300px; width: 650px; height: 372px; }
  .card-front .team-name {
    position: absolute; left: 40px; top: 88px;
    white-space: nowrap;
    color: var(--white); font-weight: 800; font-size: 52px; letter-spacing: .5px;
  }
  .card-front .tagline {
    position: absolute; left: 0; right: 40px; top: 225px; text-align: center;
    color: var(--grey); font-weight: 600; font-size: 23px;
  }
  .card-front .url {
    position: absolute; left: 34px; bottom: 30px;
    color: var(--grey); font-size: 20px; font-weight: 600;
  }
  .card-front .url span { color: var(--red); }

  /* Back card */
  .card-back { left: 770px; top: 170px; width: 380px; height: 665px; }
  .card-back .team-name {
    position: absolute; right: 40px; top: 34px; text-align: right;
    color: var(--white); font-weight: 800; font-size: 32px; line-height: 1.05;
  }
  .card-back .contact { position: absolute; left: 30px; top: 410px; color: var(--grey); }
  .contact .person-name { color: var(--red); font-size: 22px; font-weight: 600; }
  .contact .person-title { color: var(--white); font-size: 17px; margin-bottom: 14px; }
  .contact dl { display: grid; grid-template-columns: 64px auto; row-gap: 4px; font-size: 13px; }
  .contact dt { color: var(--red); }
  .contact dd { color: var(--white); }
  .contact .address { grid-column: 1 / 3; color: var(--white); line-height: 1.35; }
</style>
</head>
<body>

<section class="card card-front">
  <svg class="swoosh" viewBox="0 0 650 372" preserveAspectRatio="none" aria-hidden="true">
    <defs>
      <linearGradient id="redFront" x1="0" y1="0" x2="1" y2="0">
        <stop offset="0" stop-color="var(--red-dark)"/>
        <stop offset="1" stop-color="var(--red)"/>
      </linearGradient>
    </defs>
    <path d="M530 0 Q645 120 605 372 L650 372 L650 0 Z" fill="url(#redFront)"/>
    <path d="M548 0 Q662 140 624 372" stroke="#000" stroke-width="6" fill="none"/>
  </svg>
  <div class="team-name">Brookvale Comets</div>
  <p class="tagline">Girl's Elite Fastpitch Softball</p>
  <p class="url">www.<span>brookvalediamondcomets</span>.org</p>
</section>

<section class="card card-back">
  <svg class="swoosh" viewBox="0 0 380 665" preserveAspectRatio="none" aria-hidden="true">
    <defs>
      <linearGradient id="redBack" x1="0" y1="0" x2="1" y2="0">
        <stop offset="0" stop-color="var(--red-dark)"/>
        <stop offset="1" stop-color="var(--red)"/>
      </linearGradient>
    </defs>
    <path d="M330 90 Q390 380 270 665 L380 665 L380 60 Z" fill="url(#redBack)"/>
    <path d="M315 110 Q375 380 250 665" stroke="#000" stroke-width="8" fill="none"/>
    <path d="M305 130 Q360 380 235 665 L225 665 Q345 380 305 130 Z" fill="var(--red-dark)"/>
  </svg>
  <div class="team-name">Brookvale<br>Comets</div>
  <div class="contact">
    <p class="person-name">Jordan Avery</p>
    <p class="person-title">Designer</p>
    <dl>
      <dt>Phone:</dt><dd>999 999 9999</dd>
      <dt>Mail:</dt><dd>info@brookvalecomets.org</dd>
      <dt>Address:</dt><dd></dd>
      <dd class="address">111 Street, Anywhere Ward,<br>Anywhere City</dd>
    </dl>
  </div>
</section>

</body>
</html>
```